Business Card Design Project - KLB

I am looking for a more sophisticated card design for my company,
"The Lumen Collective"

We are a consultancy focused on strategy and change in Associations and professional organisations.

I am a lawyer and psychologist with a PhD and so am looking for something that communicates seriousness and credibility but also quirky creative solutions for strategic problems, which is my field of speciality.

I am looking for something that is quietly spoken, rather than loud colours ('credible' and 'creative' are the two adjectives that I think of as competing here).

I particularly like an embossed card style - heavy white card with plain white or white and black or white and grey text.

The key logo image for the company is a question mark and I am open to suggestions and ideas on design.

I have attached a file that includes a couple of styles that have caught my eye and my thoughts on them. Hopefully they communicate what I'm looking for.
Updates

Thank you for all the great suggestions and designs.

I really appreciated the effort and creative energy you put into your designs. I have now closed the project after selecting a design and advising the successful designer of the card that I am happy with.

Regards

Target Market(s)

Organisations (CEO's and Boards), Governments, Legal professionals, Membership Associations and aspiring professionals.

Industry/Entity Type

Lawyer

Requirements
Must have
• The key logo element is a question mark (?) and this needs to be incorporated.

Embossed style - cut outs or other design ideas interest me too.

The attached file has a number of sample ideas and comments on each one that I like.
Should not have
• I like crisp, modern fonts (Myriads etc...) and do not like embellished fonts or Times etc...

Files

```html
<!DOCTYPE html>
<html lang="en">
<head>
<meta charset="utf-8">
<title>The Lumen Collective – Business Card</title>
<link rel="stylesheet" href="https://fonts.googleapis.com/css2?family=Arimo&family=Mulish:wght@400;700&family=Questrial&display=swap">
<style>
  :root {
    --paper: #ffffff;
    --ink: #111111;
    --card-black: #000000;
    --accent: #d9492a;
    --white: #ffffff;
    --border: #333333;
  }
  * { margin: 0; padding: 0; box-sizing: border-box; }
  html, body { width: 900px; height: 1200px; overflow: hidden; background: var(--paper); }
  .sheet { position: relative; width: 900px; height: 1200px; }

  .side-label {
    position: absolute; left: 162px;
    font-family: "Arimo", Arial, sans-serif; font-size: 23px; color: var(--ink);
  }
  .side-label--back { top: 104px; }
  .side-label--front { top: 633px; }

  .card { position: absolute; overflow: hidden; }
  .card--back { left: 162px; top: 150px; width: 608px; height: 368px; background: var(--paper); border: 1px solid var(--border); }
  .card--front { left: 161px; top: 683px; width: 608px; height: 367px; background: var(--card-black); }
  .card__art { position: absolute; left: 0; top: 0; }

  .contact { position: absolute; left: 289px; top: 74px; font-family: "Mulish", "Century Gothic", sans-serif; color: var(--ink); }
  .contact__name { font-size: 22px; font-weight: 700; line-height: 28px; letter-spacing: 0.2px; }
  .contact__title { font-size: 17.5px; line-height: 22px; margin-bottom: 27px; }
  .contact__company { font-size: 16.5px; font-weight: 700; line-height: 21px; }
  .contact__line { font-size: 16.5px; line-height: 21.5px; display: flex; }
  .contact__line--gap { margin-top: 15px; }
  .contact__key { width: 15px; display: inline-block; }
  .contact__sep { margin: 0 4px 0 2px; }
  .contact__indent { padding-left: 42px; }
  .contact__icon { width: 16px; height: 12px; margin-top: 5px; margin-right: 1px; }

  .wordmark {
    position: absolute; left: 266px; top: 172px;
    font-family: "Questrial", "Century Gothic", sans-serif;
    font-size: 31px; color: var(--white); letter-spacing: 0.3px; white-space: nowrap;
  }
</style>
</head>
<body>
<main class="sheet">
  <p class="side-label side-label--back">back</p>
  <section class="card card--back" aria-label="Card back">
    <svg class="card__art" width="608" height="368" viewBox="0 0 608 368">
      <circle cx="52" cy="183" r="217" fill="none" stroke="var(--accent)" stroke-width="2"/>
      <circle cx="85" cy="75" r="63" fill="none" stroke="var(--accent)" stroke-width="2.5"/>
      <circle cx="57" cy="75" r="35" fill="none" stroke="var(--ink)" stroke-width="4.5"/>
    </svg>
    <div class="contact">
      <p class="contact__name">Dr. Mara Ellison</p>
      <p class="contact__title">Director</p>
      <p class="contact__company">The Lumen Collective</p>
      <p class="contact__line"><span class="contact__key">E</span><span class="contact__sep">:::</span>mara@lumencollective.com.au</p>
      <p class="contact__line contact__line--gap"><span class="contact__key">M</span><span class="contact__sep">:::</span>+61400 318 742</p>
      <p class="contact__line"><span class="contact__key">P</span><span class="contact__sep">:::</span>+612 9000 4615</p>
      <p class="contact__line">
        <svg class="contact__icon" viewBox="0 0 16 12" aria-label="Post"><rect x="0.5" y="0.5" width="15" height="11" fill="none" stroke="var(--ink)"/><path d="M0.5 0.5 L8 7 L15.5 0.5" fill="none" stroke="var(--ink)"/></svg>
        <span class="contact__sep">:::</span>P.O. Box 1184, Kellan Heights,
      </p>
      <p class="contact__line contact__indent">Harbourside, Australia 2190</p>
    </div>
  </section>

  <p class="side-label side-label--front">front</p>
  <section class="card card--front" aria-label="Card front">
    <svg class="card__art" width="608" height="367" viewBox="0 0 608 367">
      <circle cx="201" cy="183" r="194" fill="none" stroke="var(--accent)" stroke-width="2"/>
      <circle cx="115" cy="190" r="105" fill="none" stroke="var(--white)" stroke-width="6"/>
    </svg>
    <p class="wordmark">the lumen collective</p>
  </section>
</main>
</body>
</html>
```